Lumo Brew Premium Matcha brand Label

This is a label design project for a luxury tea brand. Feel free to be creative within the guidelines.
Attached to this project is a document called “Private Label Design Requirements” with the design guidelines and template. There is another document called "Lumo Brew Packaging Instructions" this has more details necessary to stick to the guidelines in the first document.

I have also attached the certifications to be included as well as different variations of the logo for you to use.

If you have any questions, I am here.
Updates

Target Market(s)

Young, active, fun, enjoy the finer things

```html
<!DOCTYPE html>
<html lang="en">
<head>
<meta charset="utf-8">
<title>Lumo Brew – Premium Organic Ceremonial Matcha Label</title>
<link rel="stylesheet" href="https://fonts.googleapis.com/css2?family=Teko:wght@400;500&family=Montserrat:wght@500;700&display=swap">
<style>
  :root {
    --backdrop: #ececec;
    --label-green: #9ccf94;
    --ring-green: #8cc585;
    --ring-green-deep: #79b872;
    --matcha-dark: #2f7a2e;
    --matcha-mid: #4f9a45;
    --matcha-light: #6fb061;
    --ink-dark: #1f3d1c;
    --paper: #ffffff;
  }
  * { margin: 0; padding: 0; box-sizing: border-box; }
  html, body {
    width: 1200px; height: 1000px; overflow: hidden;
    background: var(--backdrop);
  }
  .label-sheet {
    position: absolute; left: 50px; top: 395px;
    width: 1100px; height: 210px;
  }
  .label-sheet svg { display: block; }
  .display-type { font-family: "Teko", "Arial Narrow", sans-serif; font-weight: 500; fill: var(--paper); }
  .body-type { font-family: "Montserrat", Arial, sans-serif; font-weight: 500; fill: var(--ink-dark); }
  .body-type.strong { font-weight: 700; }
  .brand-name { font-family: "Teko", "Arial Narrow", sans-serif; font-weight: 500; fill: var(--ink-dark); }
</style>
</head>
<body>
  <section class="label-sheet" aria-label="Lumo Brew matcha tin label">
    <svg width="1100" height="210" viewBox="0 0 1100 210" xmlns="http://www.w3.org/2000/svg">
      <defs>
        <radialGradient id="matchaWash" cx="50%" cy="50%" r="50%">
          <stop offset="0%" stop-color="var(--matcha-mid)"/>
          <stop offset="55%" stop-color="var(--matcha-dark)"/>
          <stop offset="85%" stop-color="var(--matcha-mid)"/>
          <stop offset="100%" stop-color="var(--matcha-light)"/>
        </radialGradient>
        <clipPath id="labelEdge"><rect width="1100" height="210"/></clipPath>
      </defs>

      <rect class="label-base" width="1100" height="210" fill="var(--label-green)"/>

      <g class="matcha-wash" clip-path="url(#labelEdge)">
        <circle cx="520" cy="105" r="190" fill="var(--ring-green)"/>
        <circle cx="520" cy="105" r="160" fill="var(--ring-green-deep)"/>
        <circle cx="520" cy="105" r="128" fill="url(#matchaWash)" role="img" aria-label="Watercolour wash of matcha green"/>
      </g>

      <rect class="safe-line" x="28" y="16" width="1012" height="164" rx="22"
            fill="none" stroke="var(--paper)" stroke-width="1.5" stroke-dasharray="5 4"/>

      <g class="brand-mark">
        <circle cx="646" cy="74" r="34" fill="var(--paper)"/>
        <text class="brand-name" x="646" y="81" font-size="19" text-anchor="middle">Lumo Brew</text>
      </g>

      <g class="product-title">
        <text class="display-type" x="446" y="122" font-size="22">PREMIUM ORGANIC</text>
        <text class="display-type" x="446" y="141" font-size="22">CEREMONIAL MATCHA</text>
        <text class="display-type" x="598" y="174" font-size="15">NET WT: 30G</text>
      </g>

      <g class="origin-info">
        <text class="body-type" x="68" y="144" font-size="8">Product of Japan</text>
        <text class="body-type" x="68" y="155" font-size="8">Distributed by Lumo Brew Co. | Harbor City</text>
        <text class="body-type" x="68" y="166" font-size="8">Certified Organic by xxxx</text>
      </g>

      <g class="instructions">
        <text class="display-type" x="754" y="50" font-size="13">PREMIUM ORGANIC JAPANESE MATCHA GREEN TEA</text>
        <text class="body-type strong" x="754" y="74" font-size="9" text-decoration="underline">Instructions</text>
        <text class="body-type" x="754" y="86" font-size="8.5">• 2 tsp of Matcha</text>
        <text class="body-type" x="754" y="98" font-size="8.5">• 2oz of Water (160-170 degrees F)</text>
        <text class="body-type" x="754" y="110" font-size="8.5">• Whisk in a W formation until frothy</text>
        <text class="body-type" x="754" y="122" font-size="8.5">• Sweeten to taste</text>
      </g>

      <g class="certifications">
        <rect x="760" y="136" width="18" height="24" fill="var(--paper)"/>
        <rect x="782" y="136" width="18" height="24" fill="var(--paper)"/>
        <circle cx="816" cy="148" r="13" fill="var(--paper)"/>
        <text class="body-type strong" x="844" y="147" font-size="10">KEEP REFRIGERATED</text>
        <text class="body-type strong" x="844" y="159" font-size="10">FOR QUALITY</text>
      </g>
    </svg>
  </section>
</body>
</html>
```